Floor Inspections and Consulting

We provide inspections and consulting services on various floor coverings, e.g. carpet, hardwood, etc. We also do expert witness work for attorneys due to floor covering failures. We current have a logo, just need it incorporated into a new design. I have examples of cards I have found on the internet that capture my attention and make a statement. I have included our original business card, which in my opinion is terrible, but it does have our logo on it.

```html
<!DOCTYPE html>
<html lang="en">
<head>
<meta charset="utf-8">
<title>Keystone Floor Inspections – Business Card</title>
<link rel="stylesheet" href="https://fonts.googleapis.com/css2?family=Marcellus+SC&family=Open+Sans:wght@400;600&display=swap">
<style>
  :root {
    --amber: #c77e2c;
    --maroon: #6a180b;
    --ink: #4a4a4a;
    --paper: #ffffff;
    --backdrop: #ece8e2;
  }
  * { box-sizing: border-box; margin: 0; padding: 0; }
  html, body { width: 1200px; height: 825px; overflow: hidden; background: var(--backdrop); }
  .card {
    position: absolute; left: 40px; top: 92px; width: 1120px; height: 640px;
    background: var(--paper); overflow: hidden;
    font-family: "Open Sans", Arial, sans-serif; color: var(--ink);
  }
  .card-shapes { position: absolute; inset: 0; }
  .brand {
    position: absolute; left: 171px; top: 92px; width: 300px; text-align: center;
    font-family: "Marcellus SC", Georgia, serif; color: var(--maroon);
    font-size: 31px; line-height: 1.15;
  }
  .brand-dot { width: 44px; height: 44px; border-radius: 50%; background: var(--maroon); margin: 0 auto 14px; }
  .tagline {
    position: absolute; left: 69px; top: 322px;
    font-family: "Marcellus SC", Georgia, serif; color: var(--amber);
    font-size: 33px; letter-spacing: 1.5px;
  }
  .person { position: absolute; right: 50px; top: 180px; text-align: right; color: var(--maroon); }
  .person-name { font-family: "Marcellus SC", Georgia, serif; font-size: 29px; letter-spacing: 2px; font-weight: 600; }
  .person-title { font-family: "Marcellus SC", Georgia, serif; font-size: 22px; letter-spacing: 4px; margin-top: 2px; }
  .contact-list { position: absolute; list-style: none; font-size: 28px; }
  .contact-list li { display: flex; align-items: center; height: 41px; }
  .contact-list svg { width: 26px; height: 26px; fill: var(--amber); flex: none; }
  .online { left: 68px; top: 443px; }
  .online svg { margin-right: 16px; }
  .phones { right: 52px; top: 406px; }
  .phones li { justify-content: flex-end; }
  .phones svg { margin-left: 30px; }
  .address {
    position: absolute; left: 0; top: 551px; width: 865px; height: 89px;
    display: flex; align-items: center; justify-content: center; gap: 16px;
    color: var(--amber); font-size: 28px;
  }
  .address svg { width: 26px; height: 30px; fill: var(--amber); }
</style>
</head>
<body>
<main class="card">
  <svg class="card-shapes" viewBox="0 0 1120 640" aria-hidden="true">
    <polygon points="0,0 1120,0 1120,270 585,270 310,0 57,270 0,270" fill="var(--amber)"/>
    <rect x="0" y="551" width="1120" height="89" fill="var(--amber)"/>
    <polygon points="0,551 792,551 865,640 57,640" fill="var(--maroon)"/>
  </svg>

  <div class="brand">
    <div class="brand-dot"></div>
    Keystone Floor<br>Inspections
  </div>

  <p class="tagline">Analysis &amp; Consulting</p>

  <div class="person">
    <p class="person-name">PERSONS NAME</p>
    <p class="person-title">PERSONS TITLE</p>
  </div>

  <ul class="contact-list online">
    <li><svg viewBox="0 0 24 24"><path d="M2 5h20v14H2z M3 6l9 7 9-7" fill="var(--amber)"/><path d="M3 6.5l9 6.5 9-6.5" fill="none" stroke="#fff" stroke-width="1.6"/></svg>aaaaaa@nnn.com</li>
    <li><svg viewBox="0 0 24 24"><circle cx="12" cy="12" r="10"/><path d="M2 12h20M12 2c-5 5-5 15 0 20M12 2c5 5 5 15 0 20M4 7h16M4 17h16" fill="none" stroke="#fff" stroke-width="1.4"/></svg>www.sssssss.com</li>
  </ul>

  <ul class="contact-list phones">
    <li>(999) 222-5555<svg viewBox="0 0 24 24"><path d="M6.6 10.8a15 15 0 0 0 6.6 6.6l2.2-2.2a1 1 0 0 1 1-.25 11.4 11.4 0 0 0 3.6.57 1 1 0 0 1 1 1V20a1 1 0 0 1-1 1A17 17 0 0 1 3 4a1 1 0 0 1 1-1h3.5a1 1 0 0 1 1 1c0 1.25.2 2.45.57 3.57a1 1 0 0 1-.25 1z"/></svg></li>
    <li>(999) 222-4444<svg viewBox="0 0 24 24"><path d="M7 1h10a2 2 0 0 1 2 2v18a2 2 0 0 1-2 2H7a2 2 0 0 1-2-2V3a2 2 0 0 1 2-2zm0 3v14h10V4z"/></svg></li>
    <li>(999) 222-3333<svg viewBox="0 0 24 24"><path d="M7 2h10v5H7z M3 8h18v9h-3v5H6v-5H3z M8 14v6h8v-6z"/></svg></li>
  </ul>

  <div class="address">
    City, State Name, 77 Street Name str.
    <svg viewBox="0 0 24 28"><path d="M12 0a10 10 0 0 0-10 10c0 7.5 10 18 10 18s10-10.5 10-18A10 10 0 0 0 12 0zm0 14a4 4 0 1 1 0-8 4 4 0 0 1 0 8z"/></svg>
  </div>
</main>
</body>
</html>
```